Business cards

We need business cards for the logo that you designed for our company. Something simple and clean.

Target Market(s)

Homeowners/ people looking for construction work

Industry/Entity Type

Construction

Contact Information for Business Card

Name: Dana Holbrit, Number: 602-547-9164, Email: HolbritBuildingGroup@mailvesta.com ROC# 846203

Font styles to use
Serif

Colors

Designer to choose colors to be used in the design.

Requirements
Must have
• On one side of the card I would like to be all of the personal information I have put above along with the company logo that I have attached.
• On the other side of the card I would like the top half of the card to be the logo and then on the bottom half I would like to have the areas of construction we focus on along with an icon that represents it like the picture I have attached.
• Areas we focus on:
• Roofing, Kitchen and bath Remodel, Water Damage, Storm Damage, Fire Damage, Insurance Specialist
• If we could arrange those in alphabetical order.
Nice to have
• I have added 2 company logos a colorful one and a black one it would be nice to see a couple different options the black logo to be more simple and sleek and the colorful logo to be more colorful

```html
<!DOCTYPE html>
<html lang="en">
<head>
<meta charset="UTF-8">
<title>Holbrit Building Group – Business Cards</title>
<link href="https://fonts.googleapis.com/css2?family=Rajdhani:wght@500;600;700&display=swap" rel="stylesheet">
<style>
  :root {
    --stage: #e2e2e2;
    --card-dark: #0d0d0d;
    --card-light: #ffffff;
    --ink: #141414;
    --ink-soft: #2a2a2a;
    --paper: #ffffff;
    --water: #6cc3ef;
    --fire: #e8452c;
    --wood: #5a4a3d;
    --band-text: #d8d8d8;
  }
  * { margin: 0; padding: 0; box-sizing: border-box; }
  html, body {
    width: 1200px; height: 1000px; overflow: hidden;
    background: var(--stage);
    font-family: "Rajdhani", Arial, sans-serif;
  }
  .stage {
    position: relative; width: 1200px; height: 1000px;
    display: flex; align-items: center; justify-content: center; gap: 40px;
  }
  .card {
    position: relative; width: 525px; height: 300px;
    border-radius: 22px; overflow: hidden;
    box-shadow: 0 6px 18px rgba(0,0,0,.18);
  }

  /* Back: services */
  .card--services { background: var(--card-dark); color: var(--paper); }
  .services__brand {
    position: absolute; top: 38px; left: 0; right: 0;
    text-align: center; font-weight: 700; font-size: 40px;
    letter-spacing: 3px; text-transform: uppercase;
  }
  .services__list {
    position: absolute; left: 22px; right: 22px; top: 130px;
    display: flex; justify-content: space-between; list-style: none;
  }
  .service { width: 76px; display: flex; flex-direction: column; align-items: center; }
  .service svg { width: 46px; height: 56px; }
  .service__label {
    margin-top: 10px; font-size: 14px; font-weight: 600;
    line-height: 1.1; text-align: center;
  }

  /* Front: contact */
  .card--contact { background: var(--card-light); color: var(--ink); }
  .contact__brand {
    position: absolute; top: 34px; left: 36px;
    display: flex; align-items: center; gap: 12px;
    font-weight: 700; font-size: 24px; letter-spacing: 1.5px; text-transform: uppercase;
  }
  .contact__brand-mark { width: 26px; height: 26px; background: var(--ink); }
  .contact__name {
    position: absolute; top: 102px; left: 36px;
    font-size: 26px; font-weight: 700;
  }
  .contact__details {
    position: absolute; top: 148px; left: 36px;
    font-size: 17px; font-weight: 500; line-height: 1.35; color: var(--ink-soft);
  }
  .contact__roc {
    position: absolute; left: 0; bottom: 32px; width: 210px; height: 34px;
    background: var(--ink); color: var(--band-text);
    font-size: 16px; font-weight: 500; letter-spacing: 1px;
    display: flex; align-items: center; padding-left: 36px;
  }
  .contact__emblem {
    position: absolute; right: 40px; bottom: 40px;
    width: 120px; height: 120px; background: var(--ink);
  }
</style>
</head>
<body>
<main class="stage">

  <section class="card card--services" aria-label="Card back with services">
    <div class="services__brand">Holbrit Building Group</div>
    <ul class="services__list">
      <li class="service">
        <svg viewBox="0 0 46 56" aria-hidden="true">
          <path d="M23 54 C10 38 2 30 2 21 A21 21 0 0 1 44 21 C44 30 36 38 23 54Z" fill="var(--paper)"/>
          <path d="M12 27 L23 14 L34 27 L30 27 L23 19 L16 27Z" fill="var(--ink)"/>
        </svg>
        <span class="service__label">Roofing</span>
      </li>
      <li class="service">
        <svg viewBox="0 0 46 56" aria-hidden="true">
          <path d="M23 54 C10 38 2 30 2 21 A21 21 0 0 1 44 21 C44 30 36 38 23 54Z" fill="var(--paper)"/>
          <rect x="14" y="11" width="18" height="20" fill="var(--wood)"/>
          <line x1="23" y1="11" x2="23" y2="31" stroke="var(--paper)" stroke-width="1"/>
        </svg>
        <span class="service__label">Kitchen and bath Remodel</span>
      </li>
      <li class="service">
        <svg viewBox="0 0 46 56" aria-hidden="true">
          <path d="M23 54 C10 38 2 30 2 21 A21 21 0 0 1 44 21 C44 30 36 38 23 54Z" fill="var(--paper)"/>
          <path d="M23 10 C18 18 15 22 15 26 A8 8 0 0 0 31 26 C31 22 28 18 23 10Z" fill="var(--water)"/>
        </svg>
        <span class="service__label">Water Damage</span>
      </li>
      <li class="service">
        <svg viewBox="0 0 46 56" aria-hidden="true">
          <path d="M23 54 C10 38 2 30 2 21 A21 21 0 0 1 44 21 C44 30 36 38 23 54Z" fill="var(--paper)"/>
          <path d="M13 25 A6 6 0 0 1 16 14 A8 8 0 0 1 31 15 A5 5 0 0 1 33 25Z" fill="var(--ink)"/>
          <path d="M22 25 L19 32 L23 30 L21 36" stroke="var(--fire)" stroke-width="2" fill="none"/>
        </svg>
        <span class="service__label">Storm Damage</span>
      </li>
      <li class="service">
        <svg viewBox="0 0 46 56" aria-hidden="true">
          <path d="M23 54 C10 38 2 30 2 21 A21 21 0 0 1 44 21 C44 30 36 38 23 54Z" fill="var(--paper)"/>
          <path d="M23 9 C26 15 31 18 31 25 A8 8 0 0 1 15 25 C15 20 18 18 19 14 C21 18 22 18 23 9Z" fill="var(--fire)"/>
        </svg>
        <span class="service__label">Fire Damage</span>
      </li>
      <li class="service">
        <svg viewBox="0 0 46 56" aria-hidden="true">
          <path d="M23 54 C10 38 2 30 2 21 A21 21 0 0 1 44 21 C44 30 36 38 23 54Z" fill="var(--paper)"/>
          <rect x="14" y="10" width="18" height="22" fill="none" stroke="var(--ink)" stroke-width="2"/>
          <g stroke="var(--ink)" stroke-width="1.5">
            <line x1="17" y1="15" x2="29" y2="15"/><line x1="17" y1="19" x2="29" y2="19"/>
            <line x1="17" y1="23" x2="29" y2="23"/><line x1="17" y1="27" x2="29" y2="27"/>
          </g>
        </svg>
        <span class="service__label">Insurance Specialist</span>
      </li>
    </ul>
  </section>

  <section class="card card--contact" aria-label="Card front with contact details">
    <div class="contact__brand"><span class="contact__brand-mark"></span>Holbrit Building Group</div>
    <h1 class="contact__name">Dana Holbrit</h1>
    <p class="contact__details">602-547-9164<br>HolbritBuildingGroup@mailvesta.com</p>
    <div class="contact__roc">ROC# 846203</div>
    <div class="contact__emblem" aria-hidden="true"></div>
  </section>

</main>
</body>
</html>
```